Verdant Loop Advisors, LLC

I am looking for a simple, clear layout with my logo prominent and embossed, on the best quality card stock available. I would like the business name and phone number included on the card as well......I dont want my name anywhere on the card and I would like my logo embossed on the card......something simple with a white back......open to designs as long as they go along with recycling symbols and green type stuff.....The address, website, cell number, fax number, and email are listed below

5374 Tillbury Fenwood Road
Larkfield, MD 20799

c. 240.555.0143 f. 240.555.0187
e. sales@verdantloopadvisors.example
w. www.verdantloopadvisors.example

Industry/Entity Type

Recycling

```html
<!DOCTYPE html>
<html lang="en">
<head>
<meta charset="utf-8">
<title>Verdant Loop Advisors, LLC – Business Card</title>
<link rel="stylesheet" href="https://fonts.googleapis.com/css2?family=Goldman:wght@400;700&family=Roboto+Condensed:wght@300&display=swap">
<style>
  :root {
    --card-white: #ffffff;
    --brand-green: #3a8f47;
    --mark-green: #3d9a45;
    --ink-dark: #2e2e2e;
    --text-light: #ffffff;
  }
  html, body {
    margin: 0;
    padding: 0;
    width: 1200px;
    height: 800px;
    overflow: hidden;
    background: var(--card-white);
  }
  .card {
    position: relative;
    width: 1200px;
    height: 800px;
    background: var(--card-white);
    overflow: hidden;
  }
  .brand-band {
    position: absolute;
    left: 0; top: 0;
    width: 1200px;
    height: 263px;
    background: var(--card-white);
  }
  .brand-dot {
    position: absolute;
    left: 50px;
    top: 58px;
    width: 160px;
    height: 160px;
    border-radius: 50%;
    background: var(--mark-green);
  }
  .brand-name {
    position: absolute;
    left: 262px;
    top: 66px;
    margin: 0;
    font-family: "Goldman", sans-serif;
    font-weight: 700;
    color: var(--ink-dark);
    line-height: 1;
    white-space: nowrap;
  }
  .brand-name .name-main {
    display: block;
    font-size: 84px;
    letter-spacing: 2px;
  }
  .brand-name .name-sub {
    display: block;
    margin-top: 18px;
    font-size: 34px;
    letter-spacing: 30px;
  }
  .info-band {
    position: absolute;
    left: 0; top: 263px;
    width: 1200px;
    height: 537px;
    background: var(--brand-green);
    color: var(--text-light);
    text-align: center;
  }
  .address {
    margin: 0;
    padding-top: 52px;
    font-family: "Goldman", sans-serif;
    font-weight: 700;
    font-style: normal;
    font-size: 46px;
    letter-spacing: 3px;
    line-height: 67px;
    white-space: nowrap;
  }
  .contact {
    margin: 30px 0 0;
    font-family: "Roboto Condensed", sans-serif;
    font-weight: 300;
    white-space: nowrap;
  }
  .contact .phones {
    display: block;
    font-size: 60px;
    line-height: 68px;
  }
  .contact .online {
    display: block;
    font-size: 50px;
    line-height: 68px;
  }
</style>
</head>
<body>
  <main class="card">
    <header class="brand-band">
      <div class="brand-dot" aria-hidden="true"></div>
      <h1 class="brand-name">
        <span class="name-main">VERDANT LOOP</span>
        <span class="name-sub">ADVISORS LLC</span>
      </h1>
    </header>
    <section class="info-band">
      <address class="address">5374 Tillbury Fenwood Road<br>Larkfield, MD 20799</address>
      <p class="contact">
        <span class="phones">c. 240.555.0143 | f. 240.555.0187</span>
        <span class="online">sales@verdantloopadvisors.example</span>
        <span class="online">www.verdantloopadvisors.example</span>
      </p>
    </section>
  </main>
</body>
</html>
```